Food Hall in San Clemente, CA by the Pacific Ocean that has 15 vendors and 2 bars

We need a web page design that highlights our food hall in San Clemente, CA. The name of the food hall is Bellwick Food Hall. Inside of the food hall there are 15 different vendors and 2 bars. The place has a beautiful patio and it is by Pacific Ocean. Most of the vendors are local to San Clemente area. The highly anticipated location is opening during the summer of 2025. Website should have a dropdown menu for the different vendors that are in the food hall and people should be able to click to their respective business website. The website should also include link to our social media channels and also a link to provide comments and subscribe for the mailing list.
Target Market(s)
Mostly residents in the San Clemente, CA and surrounding areas. Couples, families and tourist alike that are looking for an exceptional dining experience that everyone can find something they like.
Industry/Entity Type
Restaurants
Coding
Coded - Design and coding required
Number of Pages Required
5+ page
Font styles to use
Look and feel

```html
<!DOCTYPE html>
<html lang="en">
<head>
<meta charset="utf-8">
<title>Bellwick Food Hall</title>
<link href="https://fonts.googleapis.com/css2?family=Marcellus&family=Poppins:wght@400;500;600;700&display=swap" rel="stylesheet">
<style>
:root{
  --sky:#aecbf0;
  --navy:#170b5f;
  --ink:#1f1470;
  --royal:#4363c8;
  --page:#f7f9fe;
  --white:#ffffff;
  --line:#5b5690;
}
*{box-sizing:border-box;margin:0;padding:0}
html,body{width:1200px;height:4205px;overflow:hidden}
body{background:var(--page);font-family:'Poppins',sans-serif;color:var(--ink);position:relative}
.abs{position:absolute}
.display{font-family:'Marcellus',serif;text-transform:uppercase;font-weight:400;color:var(--ink)}
a{color:inherit;text-decoration:none}

/* header */
.topbar{left:0;top:0;width:1200px;height:114px;background:var(--sky)}
.phone{left:60px;top:42px;display:flex;align-items:center;gap:14px;font-size:12px}
.brand{left:0;width:1200px;top:12px;text-align:center;font-size:42px;line-height:48px}
.social{right:66px;top:48px;display:flex;gap:12px;align-items:center}
.social span{width:15px;height:15px;border-radius:50%;background:var(--ink);display:block}
.nav{left:0;top:134px;width:1200px;display:flex;justify-content:center;gap:0;font-size:12.5px;text-transform:uppercase;font-weight:500}
.nav a{padding:0 15px;border-left:2px solid var(--ink);line-height:13px}
.nav a:first-child{border-left:none}
.nav a.active{position:relative}
.nav a.active::after{content:"";position:absolute;left:15px;right:15px;top:22px;height:2px;background:var(--ink)}

/* hero */
.hero-title{left:73px;top:240px;font-size:46px;line-height:53px}
.hero-dots{left:862px;top:259px;display:flex;gap:8px}
.hero-dots div{width:62px;height:62px;border-radius:50%;display:flex;align-items:center;justify-content:center}
.card{border-radius:14px;overflow:hidden}
.card-text{color:var(--white)}
.eyebrow{font-family:'Marcellus',serif;text-transform:uppercase;font-size:16px}
.btn{display:inline-flex;align-items:center;justify-content:center;background:var(--navy);color:var(--white);font-size:11.5px;font-weight:500;height:42px}
.btn-ghost{border:1px solid var(--navy);background:transparent;color:var(--navy)}

/* welcome */
.welcome{left:73px;top:986px;width:717px;height:431px;background:var(--sky);border-radius:18px}
.welcome h2{position:absolute;left:31px;top:32px;font-size:28px}
.welcome .btn{position:absolute;left:31px;top:90px;width:168px;height:45px;font-size:11.5px}
.pillar{position:absolute;top:164px;width:250px}
.pillar h3{font-size:16px;margin-top:14px;line-height:19px}
.pillar p{font-size:11.4px;line-height:22.7px;margin-top:10px}

.features{left:0;top:1480px;width:1200px}
.feature{position:absolute;width:220px;text-align:center;font-size:14px;line-height:17px}
.feature h4{font-size:17px;margin:28px 0 18px}

.vendors-title{left:617px;top:1796px;font-size:28px}
.vendor-list{left:617px;top:1857px;width:504px;list-style:none}
.vendor-list li{height:47px;border-bottom:1.5px solid var(--line);display:flex;justify-content:space-between;align-items:center;padding:0 10px;font-family:'Marcellus',serif;text-transform:uppercase;font-size:16px;padding-top:12px}

.team-label{left:62px;top:2267px;font-size:12px;text-transform:uppercase;font-weight:500}
.team-title{left:62px;top:2287px;font-size:29px;line-height:32px}
.team-copy{left:611px;top:2262px;width:525px;font-size:14.6px;line-height:22.8px}
.member{position:absolute;top:2433px;width:255px}
.member .photo{height:235px}
.member h5{font-family:'Marcellus',serif;text-transform:uppercase;font-weight:400;font-size:18px;line-height:19px;margin-top:29px;color:#6c6a8c}
.member p{font-size:12.4px;line-height:21px;color:#6c6a8c}

.reviews{left:73px;top:2832px;width:1054px;height:483px;background:var(--sky);border-radius:20px}
.quote{position:absolute;left:31px;top:146px;width:600px;font-size:21px;line-height:24.5px}

.calendar{left:47px;top:3398px;width:1104px;height:323px;border-radius:14px;overflow:hidden}

.footer{left:0;top:3766px;width:1200px;height:439px;background:var(--navy);color:var(--white)}
</style>
</head>
<body>

<header>
  <div class="abs topbar"></div>
  <div class="abs phone">
    <svg width="32" height="32" viewBox="0 0 24 24" aria-hidden="true"><path fill="#1f1470" d="M6.6 10.8a15.1 15.1 0 0 0 6.6 6.6l2.2-2.2a1 1 0 0 1 1-.25 11.4 11.4 0 0 0 3.6.57 1 1 0 0 1 1 1V20a1 1 0 0 1-1 1A17 17 0 0 1 3 4a1 1 0 0 1 1-1h3.5a1 1 0 0 1 1 1 11.4 11.4 0 0 0 .57 3.6 1 1 0 0 1-.25 1z"/></svg>
    <span>555-555-555</span>
  </div>
  <div class="abs brand display">Bellwick<br>Food Hall</div>
  <div class="abs social">
    <span aria-label="Social channel"></span><span aria-label="Social channel"></span><span aria-label="Social channel"></span><span aria-label="Social channel"></span>
    <svg width="17" height="13" viewBox="0 0 17 13" aria-label="Email"><rect x="1" y="1" width="15" height="11" rx="1.5" fill="none" stroke="#1f1470" stroke-width="1.5"/><path d="M1.5 2l7 5.5 7-5.5" fill="none" stroke="#1f1470" stroke-width="1.5"/></svg>
  </div>
  <nav class="abs nav">
    <a class="active" href="#">Home</a><a href="#">Events &amp; Promotions</a><a href="#">Location &amp; Hours</a><a href="#">Menu Highlights</a><a href="#">Vendor Showcase</a>
  </nav>
</header>

<section class="hero">
  <h1 class="abs hero-title display">Savor the flavor at<br>Bellwick Food Hall</h1>
  <div class="abs hero-dots">
    <div role="img" aria-label="Guest dining on the patio" style="background:linear-gradient(160deg,#6a7ea0,#b8453c)"></div>
    <div style="background:#e8eefb"><svg width="26" height="30" viewBox="0 0 26 30"><path d="M13 2C8 10 5 14 5 19a8 8 0 0 0 16 0c0-5-3-9-8-17z" fill="#170b5f"/><path d="M14 12l-4 8h3l-1 5 4-8h-3z" fill="#fff"/></svg></div>
    <div role="img" aria-label="Vendor counter" style="background:linear-gradient(160deg,#3b2a1c,#c49a5c)"></div>
    <div style="background:#7fa3e6"><svg width="28" height="28" viewBox="0 0 28 28"><path d="M6 23C6 11 13 5 23 5c0 11-6 17-17 18z" fill="#170b5f"/><path d="M6 23L17 12" stroke="#7fa3e6" stroke-width="1.6"/></svg></div>
  </div>

  <div class="abs card" style="left:73px;top:386px;width:516px;height:455px" role="img" aria-label="Table set with dumplings, pasta and grilled dishes">
    <div style="position:absolute;inset:0;background:linear-gradient(135deg,#5a4a3c 0%,#8d8a6c 35%,#c9b48a 60%,#6e6458 100%)"></div>
    <div class="card-text" style="position:absolute;left:25px;top:30px">
      <div class="eyebrow">A Culinary Journey</div>
      <div style="font-size:14px;margin-top:2px">Taste the best of San Clemente</div>
    </div>
    <a class="btn" style="position:absolute;left:26px;top:384px;width:150px">Explore Vendors</a>
    <a class="btn" style="position:absolute;left:230px;top:384px;width:130px;background:transparent;border:1px solid var(--navy);color:var(--navy)">Join Us</a>
  </div>

  <div class="abs card" style="left:610px;top:386px;width:517px;height:258px" role="img" aria-label="Chef seasoning a stone bowl of vegetables">
    <div style="position:absolute;inset:0;background:linear-gradient(120deg,#2e2a30 0%,#5d5560 45%,#a3806c 75%,#3a3338 100%)"></div>
    <div class="card-text" style="position:absolute;left:26px;top:24px">
      <div class="eyebrow">Unique Vendors</div>
      <div style="font-size:14px">15 diverse culinary experiences</div>
      <div style="display:flex;gap:6px;margin-top:12px">
        <span style="width:32px;height:32px;border-radius:50%;background:#c9a060;border:2px solid #fff"></span>
        <span style="width:32px;height:32px;border-radius:50%;background:#a85a3a;border:2px solid #fff"></span>
        <span style="width:32px;height:32px;border-radius:50%;background:#d8c8b8;border:2px solid #fff"></span>
      </div>
    </div>
    <a class="btn" style="position:absolute;left:26px;top:188px;width:152px">Visit Us</a>
  </div>

  <div class="abs card card-text" style="left:610px;top:662px;width:251px;height:179px;background:var(--navy);padding:24px 26px">
    <div style="font-size:29px;line-height:32px">15</div>
    <div style="font-size:11.5px;font-weight:600">Vendors</div>
    <div style="font-size:11.5px;position:absolute;left:26px;top:135px">Oceanfront Dining</div>
  </div>
  <div class="abs card card-text" style="left:877px;top:662px;width:250px;height:179px;background:var(--royal);padding:24px 26px">
    <div style="font-size:29px;line-height:32px">2</div>
    <div style="font-size:11.5px;font-weight:600">Bars</div>
    <div style="font-size:11.5px;line-height:22px;position:absolute;left:26px;top:110px;width:190px">Enjoy refreshing drinks with a view</div>
  </div>
</section>

<section>
  <div class="abs welcome">
    <h2 class="display">Welcome to Bellwick Food Hall</h2>
    <a class="btn">Explore Local Flavors</a>
    <div class="pillar" style="left:31px">
      <svg width="32" height="32" viewBox="0 0 32 32"><circle cx="16" cy="16" r="14.5" fill="none" stroke="#1f1470" stroke-width="1.6"/><path d="M11 21L21 11M13 11h8v8" fill="none" stroke="#1f1470" stroke-width="1.6"/></svg>
      <h3 class="display">Our Mission</h3>
      <p>At Bellwick Food Hall, we aim to create a vibrant culinary hub that celebrates the rich flavors of San Clemente. Our mission is to foster community connections through diverse food experiences, showcasing local vendors and their unique offerings.</p>
    </div>
    <div class="pillar" style="left:312px">
      <svg width="32" height="32" viewBox="0 0 32 32"><circle cx="16" cy="16" r="14.5" fill="none" stroke="#1f1470" stroke-width="1.6"/><path d="M11 21L21 11M13 11h8v8" fill="none" stroke="#1f1470" stroke-width="1.6"/></svg>
      <h3 class="display">Community-Driven<br>Experience</h3>
      <p>We believe in the power of local ingredients and the stories behind them. Each vendor brings a piece of San Clemente's culture to the table, ensuring an authentic taste of our community.</p>
    </div>
  </div>
  <div class="abs card" role="img" aria-label="Waiter presenting covered dishes and wine" style="left:811px;top:986px;width:316px;height:431px;border-radius:18px;background:linear-gradient(160deg,#c48c80 0%,#9a6a60 40%,#2a2630 75%,#d8d6dc 100%)"></div>
</section>

<section class="abs features">
  <div class="feature" style="left:77px">
    <svg width="46" height="46" viewBox="0 0 46 46"><circle cx="23" cy="23" r="20" fill="none" stroke="#1f1470" stroke-width="3" stroke-dasharray="100 6 4 6"/><path d="M23 14v18M14 23h18" stroke="#1f1470" stroke-width="3.4"/></svg>
    <h4 class="display">Ocean Views</h4>
    <p>Enjoy your meal with breathtaking views of the Pacific Ocean, enhancing your dining experience.</p>
  </div>
  <div class="feature" style="left:352px">
    <svg width="46" height="46" viewBox="0 0 46 46"><circle cx="23" cy="23" r="20" fill="none" stroke="#1f1470" stroke-width="3" stroke-dasharray="100 6 4 6"/><path d="M23 14v18M14 23h18" stroke="#1f1470" stroke-width="3.4"/></svg>
    <h4 class="display">Local Flavors</h4>
    <p>Savor the essence of San Clemente with dishes crafted from locally sourced ingredients.</p>
  </div>
  <div class="feature" style="left:627px">
    <svg width="46" height="46" viewBox="0 0 46 46"><circle cx="23" cy="23" r="20" fill="none" stroke="#1f1470" stroke-width="3" stroke-dasharray="100 6 4 6"/><path d="M23 14v18M14 23h18" stroke="#1f1470" stroke-width="3.4"/></svg>
    <h4 class="display">Culinary Diversity</h4>
    <p>Experience a wide range of cuisines that reflect the vibrant tapestry of our community.</p>
  </div>
  <div class="feature" style="left:902px">
    <svg width="46" height="46" viewBox="0 0 46 46"><circle cx="23" cy="23" r="20" fill="none" stroke="#1f1470" stroke-width="3" stroke-dasharray="100 6 4 6"/><path d="M23 14v18M14 23h18" stroke="#1f1470" stroke-width="3.4"/></svg>
    <h4 class="display">Join the Community</h4>
    <p>Join us as we bring together food lovers and local artisans in a space designed for connection and celebration.</p>
  </div>
</section>

<section>
  <div class="abs card" role="img" aria-label="Glass jars of baked treats on a counter" style="left:73px;top:1792px;width:516px;height:313px;border-radius:18px;background:linear-gradient(120deg,#e89a3a 0%,#c7722a 40%,#f0c080 65%,#7a4a22 100%)"></div>
  <h2 class="abs vendors-title display">Explore our unique vendors</h2>
  <ul class="abs vendor-list">
    <li>Tacos al Pastor<svg width="14" height="14" viewBox="0 0 14 14"><path d="M2 12L12 2M5 2h7v7" fill="none" stroke="#1f1470" stroke-width="1.4"/></svg></li>
    <li>Fresh Sushi Rolls<svg width="14" height="14" viewBox="0 0 14 14"><path d="M2 12L12 2M5 2h7v7" fill="none" stroke="#1f1470" stroke-width="1.4"/></svg></li>
    <li>Artisan Gelato<svg width="14" height="14" viewBox="0 0 14 14"><path d="M2 12L12 2M5 2h7v7" fill="none" stroke="#1f1470" stroke-width="1.4"/></svg></li>
    <li>Gourmet Burgers<svg width="14" height="14" viewBox="0 0 14 14"><path d="M2 12L12 2M5 2h7v7" fill="none" stroke="#1f1470" stroke-width="1.4"/></svg></li>
    <li>Vegan Bowls<svg width="14" height="14" viewBox="0 0 14 14"><path d="M2 12L12 2M5 2h7v7" fill="none" stroke="#1f1470" stroke-width="1.4"/></svg></li>
  </ul>
</section>

<section>
  <div class="abs team-label">Meet our team</div>
  <h2 class="abs team-title display">The culinary artists behind<br>Bellwick Food Hall</h2>
  <p class="abs team-copy">At Bellwick Food Hall, our talented team is the heart of our culinary experience. From innovative chefs to dedicated managers, each member plays a vital role in bringing local flavors to life. Get to know the passionate individuals who are committed to making your dining experience unforgettable.</p>
  <div class="member" style="left:65px"><div class="photo" role="img" aria-label="Portrait of the head chef" style="background:linear-gradient(160deg,#d8d8d8,#5a5a60)"></div><h5>Chef Lena Harwood</h5><p>Head Chef and Culinary Innovator</p></div>
  <div class="member" style="left:337px"><div class="photo" role="img" aria-label="Portrait of the sous chef at a desk" style="background:linear-gradient(160deg,#e6ece8,#6a7a70)"></div><h5>Chef Owen Pratt</h5><p>Sous Chef and Flavor Specialist</p></div>
  <div class="member" style="left:609px"><div class="photo" role="img" aria-label="Portrait of the operations manager by the sea" style="background:linear-gradient(170deg,#5cc4e8,#c89a84)"></div><h5 style="margin-top:9px">Manager Clara<br>Whitfield</h5><p>Operations Manager and Guest Experience Advocate</p></div>
  <div class="member" style="left:880px"><div class="photo" role="img" aria-label="Pastry chef looking out over a mountain lake" style="background:linear-gradient(180deg,#c8c4cc,#4a5060 55%,#2c3440)"></div><h5>Chef Milo Duarte</h5><p>Pastry Chef and Dessert Creator</p></div>
</section>

<section class="abs reviews">
  <div class="display" style="position:absolute;left:31px;top:30px;font-size:16px">What our visitors are saying</div>
  <div style="position:absolute;right:31px;top:30px;display:flex">
    <span style="width:34px;height:34px;border-radius:50%;background:#d49a4a;border:2px solid #fff"></span>
    <span style="width:34px;height:34px;border-radius:50%;background:#e0a040;border:2px solid #fff;margin-left:-4px"></span>
    <span style="width:34px;height:34px;border-radius:50%;background:#b8704a;border:2px solid #fff;margin-left:-4px"></span>
  </div>
  <p class="quote display">The atmosphere at Bellwick Food Hall is electric! I loved trying the fish tacos from the coastal vendor—so fresh and flavorful. Can't wait to come back for more!</p>
  <svg style="position:absolute;left:31px;top:274px" width="136" height="22" viewBox="0 0 136 22">
    <g fill="#170b5f"><path id="st" d="M10 1l2.6 6.3 6.8.5-5.2 4.4 1.6 6.6L10 15.3 4.2 18.8l1.6-6.6L.6 7.8l6.8-.5z"/><use href="#st" x="28"/><use href="#st" x="56"/><use href="#st" x="84"/><use href="#st" x="112"/></g>
  </svg>
  <div class="display" style="position:absolute;left:31px;top:403px;font-size:16px">Nora Ellison</div>
  <div style="position:absolute;left:31px;top:428px;font-size:14px;font-weight:500">Food Enthusiast, San Clemente</div>
  <div role="img" aria-label="Swans floating on the ocean" style="position:absolute;left:684px;top:106px;width:339px;height:345px;border-radius:14px;background:linear-gradient(180deg,#9aaab8 0%,#6e8498 45%,#4a6478 100%)"></div>
</section>

<section class="abs calendar" role="img" aria-label="Close-up of a smiling guest behind the announcement">
  <div style="position:absolute;inset:0;background:linear-gradient(90deg,#2a1e1c 0%,#3c2a26 40%,#6a4a3e 70%,#2c201e 100%)"></div>
  <h2 class="display" style="position:absolute;left:45px;top:38px;font-size:45px;color:#fff">Mark your calendars!</h2>
  <p style="position:absolute;left:44px;top:116px;width:430px;font-size:14px;line-height:22.5px;color:#fff">Join us for the grand opening of Bellwick Food Hall this summer and dive into a world of local flavors and culinary delights.</p>
  <a class="btn" style="position:absolute;left:44px;top:212px;width:203px;height:46px">Get Ready!</a>
</section>

<footer class="abs footer">
  <div style="position:absolute;left:36px;top:65px;font-size:26px;font-weight:700">Bellwick Food Hall</div>
  <a style="position:absolute;left:612px;top:76px;font-size:14px;font-weight:500;border-bottom:1.5px solid #fff;padding-bottom:3px">Home</a>
  <div class="display" style="position:absolute;left:36px;top:176px;font-size:20px;line-height:24px;color:#fff">This is the text area<br>for this paragraph.</div>
  <a style="position:absolute;left:123px;top:246px;font-size:12px;text-decoration:underline">Learn more</a>
  <div class="display" style="position:absolute;left:612px;top:186px;font-size:16px;color:#fff">Contact</div>
  <div style="position:absolute;left:612px;top:214px;font-size:14px;line-height:23px;font-weight:500">hello@bellwickhall.com<br>+555 5555 5555</div>
  <div class="display" style="position:absolute;left:900px;top:186px;font-size:16px;color:#fff">Address</div>
  <div style="position:absolute;left:900px;top:214px;font-size:14px;line-height:23px;font-weight:500">Street, Maryland,<br>United States</div>
  <div style="position:absolute;left:36px;top:372px;width:1128px;height:1px;background:rgba(255,255,255,.35)"></div>
  <div style="position:absolute;left:36px;top:394px;font-size:11px;font-weight:500">© 2025 All Rights Reserved | Company Name</div>
</footer>

</body>
</html>
```